New Zealand Export company needs business cards

We need new business cards to match our new logo for a company based in New Zealand who deal specifically with the Pacific Islands. We source, consolidate and ship products out of New Zealand to the Pacific Islands. Will attach our old ones and also new logo.
Would like the Islands we deal with and the areas of work we have access to, to be included on the business cards.

Contact Information for Business Card

T +64 9 571 3048
F +64 9 571 6285
12-18 Kowhai Lane, Ardmore, 2582
PO Box 814, Ardmore, Auckland 2586, New Zealand
www.falconfreight.example.nz
E sales@falconfreight.example.nz

Font styles to use
Sans Serif

Colors
85abd2
33a6d7
ffffff

Requirements
Must have
• A company of PWM

```html
<!DOCTYPE html>
<html lang="en">
<head>
<meta charset="utf-8">
<title>Falcon Freight – Business Card Presentation</title>
<link rel="stylesheet" href="https://fonts.googleapis.com/css2?family=Lexend:wght@400;500;600;700&family=Roboto+Condensed:wght@400&display=swap">
<style>
  :root {
    --sheet: #f4f7fa;
    --card-grey: #c8ced6;
    --white: #ffffff;
    --band-white: #f4f5f7;
    --navy: #2b3580;
    --brand-blue: #1f5fae;
    --sky: #3bbfec;
    --line-blue: #33a6d7;
    --fold-teal: #1a7f9c;
    --label: #111111;
  }
  html, body {
    margin: 0;
    padding: 0;
    overflow: hidden;
    background: var(--sheet);
  }
  .sheet {
    position: relative;
    width: 1200px;
    height: 1200px;
    background: var(--sheet);
    overflow: hidden;
  }
  .side-label {
    position: absolute;
    margin: 0;
    font-family: "Roboto Condensed", sans-serif;
    font-weight: 400;
    font-size: 42px;
    line-height: 1;
    color: var(--label);
  }
  .side-label--front { left: 176px; top: 18px; }
  .side-label--back { left: 176px; top: 402px; }
  .side-label--image { left: 40px; top: 772px; }
  .card {
    position: absolute;
    left: 256px;
    width: 528px;
    display: block;
  }
  .card--front { top: 101px; height: 301px; }
  .card--back { top: 468px; height: 296px; }
  .card--image { top: 836px; height: 296px; }
  .card text { font-family: "Lexend", sans-serif; }
  .holder-name { font-size: 25px; font-weight: 600; fill: var(--navy); }
  .holder-role { font-size: 12.5px; font-weight: 500; fill: var(--white); }
  .address { font-size: 13px; font-weight: 500; fill: var(--navy); }
  .brand-name { font-size: 20px; font-weight: 700; fill: var(--brand-blue); letter-spacing: 1px; }
  .ribbon-key { font-size: 16px; font-weight: 700; fill: var(--white); }
  .ribbon-value { font-size: 13.5px; font-weight: 600; fill: var(--white); }
  .web-address { font-size: 13px; font-weight: 600; fill: var(--navy); }
  .web-address--light { fill: var(--white); }
</style>
</head>
<body>
<main class="sheet">

  <h2 class="side-label side-label--front">front</h2>
  <svg class="card card--front" viewBox="0 0 440 251" aria-label="Business card front">
    <rect class="card-base" width="440" height="251" fill="var(--card-grey)"/>
    <polygon class="card-white-panel" points="0,13 193,13 335,251 0,251" fill="var(--white)"/>
    <polygon class="name-banner" points="192,0 440,0 440,60 228,60" fill="var(--sky)"/>
    <text class="holder-name" x="242" y="32">Tessa Ngata</text>
    <text class="holder-role" x="242" y="47">Sales Manager</text>

    <g class="address-block" text-anchor="end">
      <text class="address" x="433" y="84">12-18 Kowhai Lane,</text>
      <text class="address" x="433" y="100">Ardmore, 2582</text>
      <text class="address" x="433" y="115">PO Box 814, Ardmore,</text>
      <text class="address" x="433" y="131">Auckland 2586,</text>
      <text class="address" x="433" y="147">New Zealand</text>
    </g>

    <g class="brand">
      <rect x="6" y="30" width="30" height="30" fill="var(--brand-blue)"/>
      <text class="brand-name" x="44" y="44">FALCON</text>
      <text class="brand-name" x="44" y="63">FREIGHT</text>
    </g>

    <g class="ribbon ribbon--phone">
      <polygon points="252,115 270,115 262,125" fill="var(--fold-teal)"/>
      <rect x="0" y="93" width="270" height="22" fill="var(--navy)"/>
      <text class="ribbon-key" x="8" y="110">T</text>
      <text class="ribbon-value" x="55" y="109">+64 9 571 3048</text>
    </g>
    <g class="ribbon ribbon--fax">
      <polygon points="274,153 292,153 284,163" fill="var(--fold-teal)"/>
      <rect x="0" y="130" width="292" height="23" fill="var(--navy)"/>
      <text class="ribbon-key" x="8" y="147">F</text>
      <text class="ribbon-value" x="55" y="146">+64 9 571 6285</text>
    </g>
    <g class="ribbon ribbon--email">
      <polygon points="300,192 318,192 310,202" fill="var(--fold-teal)"/>
      <rect x="0" y="169" width="318" height="23" fill="var(--navy)"/>
      <text class="ribbon-key" x="8" y="186">E</text>
      <text class="ribbon-value" x="55" y="185">sales@falconfreight.example.nz</text>
    </g>
    <g class="ribbon ribbon--web">
      <polygon points="326,231 344,231 336,241" fill="var(--fold-teal)"/>
      <rect x="0" y="208" width="344" height="23" fill="var(--navy)"/>
      <text class="ribbon-value" x="51" y="224">www.falconfreight.example.nz</text>
    </g>
  </svg>

  <h2 class="side-label side-label--back">back</h2>
  <svg class="card card--back" viewBox="0 0 440 247" aria-label="Business card back">
    <rect class="card-base" width="440" height="247" fill="var(--card-grey)"/>
    <polygon class="accent-wedge" points="0,97 76,97 100,154 0,154" fill="var(--sky)"/>
    <polygon class="brand-band" points="78,90 440,90 440,154 103,154" fill="var(--band-white)"/>
    <g class="brand">
      <rect x="130" y="107" width="30" height="30" fill="var(--brand-blue)"/>
      <text class="brand-name" x="168" y="121">FALCON</text>
      <text class="brand-name" x="168" y="140">FREIGHT</text>
    </g>
    <line x1="0" y1="166" x2="124" y2="166" stroke="var(--line-blue)" stroke-width="1"/>
    <line x1="318" y1="166" x2="440" y2="166" stroke="var(--line-blue)" stroke-width="1"/>
    <text class="web-address" x="221" y="170" text-anchor="middle">www.falconfreight.example.nz</text>
  </svg>

  <h2 class="side-label side-label--image">image back</h2>
  <svg class="card card--image" viewBox="0 0 440 247" aria-label="Business card back with photo">
    <defs>
      <linearGradient id="beach-tones" x1="0" y1="0" x2="0" y2="1">
        <stop offset="0" stop-color="#3f72bd"/>
        <stop offset="0.35" stop-color="#4f7f6a"/>
        <stop offset="0.62" stop-color="#2a62b4"/>
        <stop offset="0.85" stop-color="#1d4f9e"/>
        <stop offset="1" stop-color="#d6d0c2"/>
      </linearGradient>
    </defs>
    <rect class="photo-area" role="img" aria-label="Tropical beach photo with palm trees, a thatched umbrella and sun loungers by blue sea" width="440" height="247" fill="url(#beach-tones)"/>
    <polygon class="accent-wedge" points="0,97 76,97 100,154 0,154" fill="var(--sky)" fill-opacity="0.55"/>
    <polygon class="brand-band" points="78,90 440,90 440,154 103,154" fill="var(--white)" fill-opacity="0.65"/>
    <g class="brand">
      <rect x="130" y="107" width="30" height="30" fill="var(--brand-blue)"/>
      <text class="brand-name" x="168" y="121">FALCON</text>
      <text class="brand-name" x="168" y="140">FREIGHT</text>
    </g>
    <line x1="0" y1="166" x2="124" y2="166" stroke="var(--line-blue)" stroke-width="1"/>
    <line x1="318" y1="166" x2="440" y2="166" stroke="var(--line-blue)" stroke-width="1"/>
    <text class="web-address web-address--light" x="221" y="170" text-anchor="middle">www.falconfreight.example.nz</text>
  </svg>

</main>
</body>
</html>
```